Christmas Sale banner ad for Watch Brand

I need a banner ad for a watch company running a christmas sale.
It should combine 3 models (images attached) and our logo. There are 2 images per model attached, feel free to choose either.
I have also added some photos with a clean background if needed.
The models are
Vantel (the one with disks for hands)
Plinto 2 (minimalist style shown in gold or white)
Brenn (jet plane themed photos)
The banner should have a black background. Text will be
Just in Time for Christmas - Up to 50% OFF!
Include a button for 'Shop Now'
Res should be 3000x2000
Men
It Company

```html
<!DOCTYPE html>
<html lang="en">
<head>
<meta charset="utf-8">
<title>Orvane Christmas Sale</title>
<link href="https://fonts.googleapis.com/css2?family=Montserrat:wght@400;500;600;700&display=swap" rel="stylesheet">
<style>
  :root {
    --bg-deep: #000000;
    --bg-mid: #1c1c1c;
    --bg-glow: #2e2e2e;
    --line: rgba(255, 255, 255, 0.55);
    --line-bright: rgba(255, 255, 255, 0.95);
    --text: #ffffff;
    --text-soft: #e6e6e6;
    --cta: #a8131b;
    --cta-edge: #7d0d13;
    --strap-brown: #3a2619;
    --strap-canvas: #4a4a44;
    --case-steel: #6b6b6b;
    --case-black: #1a1a1a;
    --dial-copper: #b5725a;
    --dial-white: #e9e9e6;
  }
  * { margin: 0; padding: 0; box-sizing: border-box; }
  html, body { width: 1200px; height: 801px; overflow: hidden; background: var(--bg-deep); }
  .banner {
    position: relative;
    width: 1200px;
    height: 801px;
    overflow: hidden;
    font-family: 'Montserrat', sans-serif;
    background:
      radial-gradient(ellipse 620px 460px at 600px 330px, var(--bg-glow) 0%, var(--bg-mid) 45%, var(--bg-deep) 100%);
  }
  .frames { position: absolute; inset: 0; width: 1200px; height: 801px; }
  .watch {
    position: absolute;
    border-radius: 60px;
  }
  .watch--vantel {
    left: 300px; top: 180px; width: 196px; height: 300px;
    background: radial-gradient(circle at 50% 48%, var(--dial-copper) 0%, #4b4039 32%, var(--case-steel) 40%, var(--strap-brown) 55%, #1e140d 100%);
    border-radius: 98px / 150px;
  }
  .watch--plinto {
    left: 512px; top: 175px; width: 176px; height: 315px;
    background: radial-gradient(circle at 50% 47%, #222 0%, #101010 30%, var(--case-black) 38%, var(--strap-canvas) 55%, #26261f 100%);
    border-radius: 88px / 157px;
  }
  .watch--brenn {
    left: 680px; top: 195px; width: 180px; height: 280px;
    background: radial-gradient(circle at 50% 38%, var(--dial-white) 0%, #cfcfcc 30%, #8a8a8a 38%, var(--strap-brown) 52%, #1a110b 100%);
    border-radius: 90px / 140px;
  }
  .offer {
    position: absolute;
    left: 316px;
    top: 613px;
    height: 58px;
    display: flex;
    align-items: center;
  }
  .brand {
    display: flex;
    align-items: center;
    gap: 8px;
    margin-right: 20px;
  }
  .brand__dot {
    width: 30px; height: 30px;
    border-radius: 50%;
    background: var(--text);
  }
  .brand__name {
    color: var(--text);
    font-weight: 700;
    font-size: 13px;
    letter-spacing: 1.5px;
  }
  .offer__copy { display: flex; flex-direction: column; gap: 4px; margin-right: 44px; }
  .offer__kicker {
    color: var(--text-soft);
    font-weight: 500;
    font-size: 13px;
    letter-spacing: 1.6px;
    text-transform: uppercase;
  }
  .offer__headline {
    color: var(--text);
    font-weight: 700;
    font-size: 20px;
    letter-spacing: 1.2px;
    text-transform: uppercase;
  }
  .cta {
    display: inline-flex;
    align-items: center;
    justify-content: center;
    width: 164px;
    height: 54px;
    background: var(--cta);
    border-bottom: 2px solid var(--cta-edge);
    border-radius: 3px;
    color: var(--text);
    font-weight: 700;
    font-size: 13px;
    letter-spacing: 1.2px;
    text-decoration: none;
    text-transform: uppercase;
  }
</style>
</head>
<body>
<main class="banner">
  <svg class="frames" viewBox="0 0 1200 801" aria-hidden="true">
    <defs>
      <linearGradient id="beam" x1="0" y1="0" x2="1" y2="1">
        <stop offset="0" stop-color="#fff" stop-opacity="0"/>
        <stop offset="0.5" stop-color="#fff" stop-opacity="0.9"/>
        <stop offset="1" stop-color="#fff" stop-opacity="0"/>
      </linearGradient>
      <radialGradient id="glint">
        <stop offset="0" stop-color="#fff" stop-opacity="1"/>
        <stop offset="1" stop-color="#fff" stop-opacity="0"/>
      </radialGradient>
    </defs>
    <g fill="none" stroke="var(--line)" stroke-width="1.5">
      <polygon points="398,160 568,330 398,500 228,330"/>
      <polygon points="600,140 790,330 600,520 410,330"/>
      <polygon points="790,135 955,300 790,465 625,300"/>
    </g>
    <g stroke="url(#beam)" stroke-width="2.5">
      <line x1="255" y1="560" x2="470" y2="345"/>
      <line x1="540" y1="500" x2="700" y2="340"/>
      <line x1="860" y1="230" x2="960" y2="330"/>
    </g>
    <g fill="url(#glint)">
      <circle cx="228" cy="330" r="12"/>
      <circle cx="790" cy="330" r="14"/>
      <circle cx="625" cy="300" r="10"/>
      <circle cx="955" cy="300" r="10"/>
    </g>
  </svg>

  <div class="watch watch--vantel" role="img" aria-label="Vantel watch with copper disc dial and brown leather strap"></div>
  <div class="watch watch--plinto" role="img" aria-label="Black aviator watch with canvas strap"></div>
  <div class="watch watch--brenn" role="img" aria-label="Minimalist white dial watch with brown leather strap"></div>

  <section class="offer">
    <div class="brand">
      <span class="brand__dot"></span>
      <span class="brand__name">ORVANE</span>
    </div>
    <div class="offer__copy">
      <p class="offer__kicker">Just in time for Christmas</p>
      <p class="offer__headline">Up to 50% off!</p>
    </div>
    <a class="cta" href="#">Shop now &nbsp;›</a>
  </section>
</main>
</body>
</html>
```